Homepage design

Hi
I m workingon hosting my website tallowbrook.net on wordpress but the new design for the homepage is not good
I need a design just for that page on how to organise things and what to put there

```html
<!DOCTYPE html>
<html lang="en">
<head>
<meta charset="utf-8">
<title>Tallowbrook – Foreign Exchange Broker</title>
<link href="https://fonts.googleapis.com/css2?family=Open+Sans:wght@400;600;700&display=swap" rel="stylesheet">
<style>
:root{
  --navy:#1b4b8f;
  --red:#d1202b;
  --blue:#2f7cc6;
  --blue-dark:#1f5fa3;
  --ink:#333;
  --muted:#666;
  --line:#dcdcdc;
  --topbar:#1f1f1f;
  --hero:#dcebf8;
  --page:#f5f5f5;
  --white:#fff;
}
*{box-sizing:border-box;margin:0;padding:0}
html,body{width:1200px;height:2204px;overflow:hidden}
body{font-family:"Open Sans",Arial,sans-serif;color:var(--ink);background:var(--white);position:relative}
section,header,footer,nav{position:absolute;left:0;width:1200px}
.abs{position:absolute}

/* top bar */
.topbar{top:0;height:30px;background:var(--topbar);color:#ddd;font-size:13px}
.topbar ul{list-style:none;display:flex;gap:22px;position:absolute;left:110px;top:6px;align-items:center}
.home-icon{width:14px;height:13px;fill:#ddd}
.lang{position:absolute;right:110px;top:5px;background:#fff;color:#333;font-size:12px;padding:1px 8px;border-radius:2px}

/* header */
.site-header{top:30px;height:110px;background:var(--white)}
.brand{left:110px;top:30px;display:flex;align-items:center;gap:12px}
.brand-dot{width:38px;height:38px;border-radius:50%;background:var(--red)}
.brand-name{font-size:36px;font-weight:700;color:var(--navy)}
.hotline{right:110px;top:42px;font-size:17px;font-weight:700;color:#333}
.hotline span{color:var(--blue)}

/* hero */
.hero{top:140px;height:260px;background:linear-gradient(#e8f2fb,var(--hero))}
.hero h1{left:110px;top:52px;font-size:40px;font-weight:400;line-height:1.25;color:#222;width:560px}
.hero h1 em{font-style:normal;color:var(--red)}
.btn{display:inline-block;color:#fff;font-weight:600;text-align:center;border-radius:4px}
.hero .btn{left:110px;top:180px;width:180px;height:42px;line-height:42px;background:var(--blue);font-size:15px;text-transform:uppercase}
.hero-art{left:690px;top:45px;width:400px;height:215px;border-radius:8px 8px 0 0;background:linear-gradient(135deg,#2a2a2a,#4a4a4a 40%,#d8e8f6 41%,#b9d3ec)}
.slider-bar{top:400px;height:36px;background:#e6e6e6;border-bottom:1px solid var(--line)}
.dots{left:490px;top:4px;width:200px;height:28px;background:#f4f4f4;border:1px solid #d0d0d0;border-radius:3px;display:flex;justify-content:center;gap:24px;align-items:center}
.dots i{width:14px;height:14px;border-radius:50%;background:#ddd;box-shadow:inset 0 1px 2px #aaa}
.dots i.on{background:#f08020}

/* intro */
.intro{top:436px;height:886px;background:var(--page);border-bottom:1px solid var(--line)}
.video{left:110px;top:91px;width:640px;height:391px;background:#000}
.video-screen{position:absolute;left:80px;top:0;width:480px;height:360px;background:#fff;display:flex;flex-direction:column;align-items:center;justify-content:center;gap:8px}
.video-screen .brand-name{font-size:56px}
.video-screen small{font-size:16px;font-weight:700;color:var(--red);letter-spacing:1px}
.video-controls{position:absolute;left:0;bottom:0;width:640px;height:31px;background:#1a1a1a;color:#ccc;font-size:11px}
.video-controls .track{position:absolute;left:0;top:0;width:640px;height:4px;background:#555}
.video-controls .track b{display:block;width:90px;height:4px;background:#c00}
.video-controls span{position:absolute;left:40px;top:10px}
.intro h2{left:110px;top:530px;font-size:28px;font-weight:400;color:var(--navy);width:640px;line-height:1.35}
.intro h2 strong{color:var(--red);font-weight:700}
.intro .copy{left:110px;top:624px;width:640px;font-size:13px;line-height:1.6;color:var(--muted)}
.intro .copy p{margin-bottom:18px}
.share{left:110px;top:812px;display:flex;gap:14px;font-size:11px}
.share span{border:1px solid #ccc;background:#fff;padding:2px 6px;border-radius:2px}
.share span b{font-weight:400;color:#888;margin-left:6px}

.quote{left:779px;top:91px;width:311px;height:458px;background:#e9e9e9;border:1px solid var(--line)}
.quote h3{font-size:17px;font-weight:600;color:var(--navy);padding:14px 14px;border-bottom:1px solid var(--line);background:#f3f3f3}
.quote .field{margin:12px 18px 0;height:34px;background:#fff;border:1px solid #ccc;color:#aaa;font-size:14px;text-align:center;line-height:32px}
.captcha{display:flex;margin:14px 18px 0;gap:10px;font-size:10px;color:#888;align-items:center}
.captcha-img{width:130px;height:40px;background:linear-gradient(90deg,#dfe6f3,#f4f6fb);border:1px solid #ccc}
.quote .btn{margin:16px 18px 0;display:block;height:44px;line-height:44px;background:var(--blue-dark);font-size:16px;font-weight:400}
.account{left:779px;top:566px;width:311px;height:56px;background:var(--red);border-radius:4px;color:#fff;display:flex;align-items:center;gap:14px;padding-left:22px}
.account svg{width:30px;height:30px}
.account strong{display:block;font-size:17px}
.account small{font-size:12px}

/* solutions */
.solutions{top:1322px;height:560px}
.solutions h2{left:110px;top:80px;font-size:38px;font-weight:600;color:#222;letter-spacing:.5px}
.solutions h2 span{color:var(--navy)}
.service{left:110px;width:620px;display:flex;gap:22px}
.service-icon{flex:none;width:92px;height:92px;display:flex;align-items:center;justify-content:center}
.service-icon.solid{background:var(--navy)}
.service-icon.light{background:#eef2f7;border:1px solid var(--line)}
.service h3{font-size:19px;font-weight:600;color:var(--navy);margin:8px 0 12px}
.service p{font-size:13px;line-height:1.6;color:var(--muted)}
.news{left:779px;top:91px;width:311px;height:453px;border:1px solid var(--line);background:#f1f1f1}
.news h3{font-size:19px;font-weight:600;color:var(--navy);padding:14px 16px;background:#fff}
.news-item{margin:12px 14px 0;background:#fff;border:1px solid var(--line);padding:10px 12px;height:152px}
.news-item h4{font-size:12px;font-weight:700;color:var(--navy);line-height:1.5;padding-bottom:8px;border-bottom:1px solid var(--line)}
.news-item p{font-size:12px;line-height:1.55;color:var(--muted);margin-top:8px}
.news a{display:block;text-align:center;font-size:12px;color:var(--blue);margin-top:14px}

/* footer */
.footer-nav{top:1930px;height:30px;background:#e4e4e4;border-top:1px solid var(--line);font-size:13px;color:#555}
.footer-nav ul{list-style:none;display:flex;gap:22px;position:absolute;left:110px;top:6px;align-items:center}
.footer-nav .home-icon{fill:#555}
.site-footer{top:1960px;height:188px;background:var(--page)}
.site-footer h4{font-size:11px;font-weight:700;color:#333;text-transform:uppercase}
.newsletter{left:110px;top:50px;font-size:12px;color:#555}
.newsletter p{margin:4px 0 16px}
.newsletter .email{width:220px;height:28px;border:1px solid #ccc;background:#fff;color:#999;font-size:12px;line-height:26px;padding-left:10px;display:inline-block}
.newsletter .go{display:inline-block;height:28px;line-height:26px;border:1px solid #ccc;background:#eee;padding:0 8px;margin-left:2px}
.links{left:488px;top:50px;font-size:12px;color:#555;border-left:1px solid var(--line);padding-left:0}
.links ul{list-style:none;margin-top:8px;line-height:1.9}
.links-divider{left:446px;top:40px;width:1px;height:100px;background:var(--line)}
.links-divider.r{left:630px}
.social{left:700px;top:50px}
.social div{display:flex;gap:6px;margin-top:14px}
.social i{width:30px;height:30px;border-radius:4px;background:#5a6d8c}
.bottombar{top:2148px;height:56px;background:#1a1a1a;color:#ccc;font-size:11px}
.bottombar p{position:absolute;left:110px;top:20px}
.bottombar p span{color:#f08020}
.bottombar ul{position:absolute;right:110px;top:20px;list-style:none;display:flex;gap:10px}
</style>
</head>
<body>

<nav class="topbar">
  <ul>
    <li><svg class="home-icon" viewBox="0 0 14 13"><path d="M7 0 0 6h2v7h4V9h2v4h4V6h2z"/></svg></li>
    <li>Personal</li><li>Business</li><li>Market Knowledge</li><li>Currency Tools</li><li>Why Tallowbrook</li>
  </ul>
  <div class="lang">English ▾</div>
</nav>

<header class="site-header">
  <div class="brand abs"><span class="brand-dot"></span><span class="brand-name">Tallowbrook</span></div>
  <div class="hotline abs">Information Hotline: <span>+44 (0)20 7946 0321</span></div>
</header>

<section class="hero">
  <h1 class="abs">We provide better <em>exchange rate than</em> banks</h1>
  <a class="btn abs">Contact us now!</a>
  <div class="hero-art abs" role="img" aria-label="Computer screen showing a rising coloured bar chart"></div>
</section>
<section class="slider-bar">
  <div class="dots abs"><i class="on"></i><i></i><i></i><i></i></div>
</section>

<section class="intro">
  <div class="video abs">
    <div class="video-screen">
      <span class="brand-name">Tallowbrook</span>
      <small>FOREIGN EXCHANGE BROKER</small>
    </div>
    <div class="video-controls"><div class="track"><b></b></div><span>▶ &nbsp; 0:00 / 1:23</span></div>
  </div>

  <h2 class="abs">AT <strong>Tallowbrook</strong> we are a foreign currency broker for private and business clients.</h2>
  <div class="copy abs">
    <p>We place our business focus on providing our clients with the most competitive rates for currency exchange and money transfers whilst executing the highest quality of client service. Strategically located in London's financial district, we have immediate access to critical market insight enabling our clients to make a quick and informed decision as to when to convert currency.</p>
    <p>Our FX specialists buy and sell currency at rates close to interbank value. We monitor the currency market, work with live rates and aim to get the best rate at the time for our clients. Dealing with a large amount of international payments brings economies of scale which allows us to achieve even better exchange rates.</p>
  </div>
  <div class="share abs"><span>Like<b>173</b></span><span>Post<b>88</b></span><span>Save<b>24</b></span></div>

  <form class="quote abs">
    <h3>Request a currency quote</h3>
    <div class="field">Fullname</div>
    <div class="field">Company</div>
    <div class="field">Telephone</div>
    <div class="field">Email</div>
    <div class="captcha"><div class="captcha-img" role="img" aria-label="Verification code image"></div><div>Get another code<br>Get an audio code</div></div>
    <div class="field">Type the words</div>
    <a class="btn">Get a quote now</a>
  </form>
  <a class="account abs">
    <svg viewBox="0 0 30 30"><rect x="3" y="13" width="24" height="15" rx="2" fill="#fff"/><path d="M8 13V9a7 7 0 0 1 14 0v4" stroke="#fff" stroke-width="3" fill="none"/></svg>
    <div><strong>Open an Account</strong><small>Authorised by the Payments Authority</small></div>
  </a>
</section>

<section class="solutions">
  <h2 class="abs"><span>TALLOWBROOK</span> SOLUTIONS</h2>
  <div class="service abs" style="top:189px">
    <div class="service-icon solid"><svg width="44" height="44" viewBox="0 0 44 44"><circle cx="22" cy="22" r="20" fill="none" stroke="#fff" stroke-width="3"/><circle cx="22" cy="17" r="6" fill="#fff"/><path d="M11 33c2-7 20-7 22 0z" fill="#fff"/></svg></div>
    <div><h3>Personal Currency Exchange</h3><p>Whether you are buying or selling overseas property or simply undertaking money transfers abroad, you need to buy the relevant foreign currency and optimise your budget. This is where we can help and offer competitive rates for both currency exchange and money transfers.</p></div>
  </div>
  <div class="service abs" style="top:360px">
    <div class="service-icon light"><svg width="40" height="34" viewBox="0 0 40 34"><rect x="2" y="8" width="36" height="24" rx="3" fill="var(--navy)"/><path d="M14 8V4h12v4" stroke="var(--navy)" stroke-width="3" fill="none"/><rect x="17" y="16" width="6" height="5" fill="#fff"/></svg></div>
    <div><h3>Business Currency Exchange</h3><p>We help you to minimise your foreign exchange risks on profit and optimise your international payment costs. Use Tallowbrook's expertise to spend less time managing your international payments and devote more time to growing your business.</p></div>
  </div>

  <aside class="news abs">
    <h3>Currency News</h3>
    <div class="news-item"><h4>International Currency Exchange News 1st February to 8th February 2013:</h4><p>Global markets report: Call us on +44 (0)20 7946 0321 or email us to info@tallowbrook.net....</p></div>
    <div class="news-item"><h4>International Currency Exchange News 1st February to 8th February 2013:</h4><p>Global markets report: Call us on +44 (0)20 7946 0321 or email us to info@tallowbrook.net....</p></div>
    <a>Sign up for Daily Rates update</a>
  </aside>
</section>

<nav class="footer-nav">
  <ul>
    <li><svg class="home-icon" viewBox="0 0 14 13"><path d="M7 0 0 6h2v7h4V9h2v4h4V6h2z"/></svg></li>
    <li>Personal</li><li>Business</li><li>Market Knowledge</li><li>Currency Tools</li><li>Why Tallowbrook</li>
  </ul>
</nav>

<footer class="site-footer">
  <div class="newsletter abs">
    <h4>Tallowbrook</h4>
    <p>Signup for newsletter &amp; special offers:</p>
    <span class="email">Email address</span><span class="go">Go</span>
  </div>
  <div class="links-divider abs"></div>
  <div class="links abs">
    <h4>Other Links</h4>
    <ul><li>Services</li><li>Exchange</li><li>Foreign Exchange</li><li>Currency Tools</li></ul>
  </div>
  <div class="links-divider r abs"></div>
  <div class="social abs">
    <h4>Stay connected :</h4>
    <div><i></i><i></i><i></i><i></i><i></i></div>
  </div>
</footer>

<footer class="bottombar">
  <p>Copyright © 2013. <span>Tallowbrook</span></p>
  <ul><li>TERMS</li><li>|</li><li>HELP</li><li>|</li><li>CONTACTS</li></ul>
</footer>

</body>
</html>
```